KORVAL RENOVATIONS AND CUSTOM BUILDS

5pages:
Home/ who we are , services offered, why us,
recent projects/ gallery , contact us

Industry/Entity Type

Design, renovations, project management

Coding

Coded - Design and coding required

Number of Pages Required

5+ page

Requirements
Should not have
• Too many colours

```html
<!DOCTYPE html>
<html lang="en">
<head>
<meta charset="utf-8">
<title>Korval Renovations and Custom Builds</title>
<link href="https://fonts.googleapis.com/css2?family=Montserrat:wght@400;500;600;700&display=swap" rel="stylesheet">
<style>
:root{
  --navy:#1c2541;
  --green:#78b72b;
  --teal:#3dbdae;
  --grey-bg:#f4f4f4;
  --text:#3c4250;
  --muted:#6b7080;
  --white:#ffffff;
}
*{box-sizing:border-box;margin:0;padding:0}
html,body{width:1200px;height:4702px;overflow:hidden}
body{font-family:'Montserrat',sans-serif;color:var(--text);background:var(--white);position:relative}
.abs{position:absolute}
.btn{position:absolute;display:flex;align-items:center;justify-content:center;background:var(--green);color:var(--white);font-size:13px;font-weight:600;border-radius:20px;text-transform:uppercase;letter-spacing:.3px}
.btn-navy{background:var(--navy)}
.section-title{position:absolute;left:0;width:1200px;text-align:center;font-size:38px;color:var(--navy);font-weight:500;letter-spacing:.5px}
.section-title b{font-weight:700}
.title-rule{position:absolute;width:40px;height:3px;background:var(--green)}

/* top bar */
.topbar{left:0;top:0;width:1200px;height:37px;background:var(--navy)}
.social-dot{position:absolute;top:7px;width:22px;height:22px;border-radius:50%;background:var(--green)}
.topbar-contact{position:absolute;top:10px;font-size:13px;color:var(--white);white-space:nowrap}
.topbar-contact b{font-weight:600}
.topbar-contact svg{vertical-align:-2px;margin-right:6px}

/* header */
.header{left:0;top:37px;width:1200px;height:77px;background:var(--white)}
.wordmark{position:absolute;font-weight:700;white-space:nowrap;letter-spacing:.3px}
.nav a{position:absolute;top:32px;font-size:13px;font-weight:600;color:var(--navy);text-decoration:none;letter-spacing:.3px;white-space:nowrap}
.nav a.active{color:var(--green)}

/* hero */
.hero{left:0;top:114px;width:1200px;height:600px;background:linear-gradient(120deg,#5a5550 0%,#9d9890 35%,#c9c6c0 60%,#8d8a86 100%)}
.hero h1{position:absolute;left:160px;top:110px;font-size:40px;line-height:46px;font-weight:500;color:var(--white);letter-spacing:.5px}
.hero h1 b{font-weight:700}

/* who we are */
.who-photo{left:172px;top:767px;width:394px;height:383px;background:linear-gradient(180deg,#b9a4c6 0%,#7f8fb0 45%,#4f5a6d 75%,#6a6f78 100%)}
.who-frame{left:186px;top:755px;width:390px;height:260px;border:2px solid var(--teal);border-bottom:none;border-left:none}
.badge{left:420px;top:992px;width:184px;height:190px;background:var(--white);border:5px solid var(--teal);text-align:center;color:var(--navy)}
.badge .num{font-size:64px;font-weight:700;line-height:1;margin-top:18px}
.badge .lbl{font-size:22px;font-weight:700;line-height:26px}
.who h2{position:absolute;left:672px;top:806px;font-size:37px;font-weight:700;color:var(--navy);letter-spacing:.5px}
.who h2 span{font-weight:500}
.who p{position:absolute;left:672px;top:870px;width:360px;font-size:21px;line-height:38px;color:var(--muted)}
.who p b{color:var(--navy);font-weight:600}

/* what we do */
.lead{position:absolute;left:0;width:1200px;text-align:center;font-size:13px;color:var(--text)}
.lead b{font-weight:700;color:var(--navy)}
.sector{position:absolute;top:1388px;width:238px;height:238px;border-radius:50%;overflow:hidden}
.sector span{position:absolute;left:0;bottom:34px;width:100%;text-align:center;color:var(--white);font-size:18px;font-weight:500;letter-spacing:.5px}

/* services */
.services{left:0;top:1716px;width:1200px;height:786px;background:var(--grey-bg)}
.card{position:absolute;width:203px;height:246px;background:var(--white);box-shadow:0 2px 8px rgba(0,0,0,.08)}
.card .ph{position:absolute;left:0;top:0;width:203px;height:150px}
.card .ic{position:absolute;left:77px;top:120px;width:48px;height:48px;border-radius:50%;background:var(--green);border:4px solid var(--white);display:flex;align-items:center;justify-content:center}
.card .nm{position:absolute;left:0;top:190px;width:100%;text-align:center;font-size:13px;font-weight:700;color:var(--navy);line-height:19px}

/* team */
.team h3{position:absolute;left:160px;font-size:23px;font-weight:700;color:var(--navy);letter-spacing:.3px}
.task{position:absolute;font-size:13px;color:var(--text);display:flex;align-items:center;gap:6px;white-space:nowrap}
.team-rule{left:160px;top:2820px;width:396px;height:1px;background:#dcdcdc}

/* why us */
.why{left:0;top:3086px;width:1200px;height:617px;background:var(--grey-bg)}
.why-ic{position:absolute;width:70px;height:70px;border-radius:50%;background:var(--navy);display:flex;align-items:center;justify-content:center}
.why-lbl{position:absolute;font-size:15px;font-weight:500;color:var(--navy);line-height:21px}

/* area */
.area h2{position:absolute;left:667px;top:3862px;font-size:37px;font-weight:700;color:var(--navy);letter-spacing:.5px}
.area h2 span{font-weight:500}
.area p{position:absolute;left:667px;top:3932px;width:380px;font-size:13px;line-height:22px;color:var(--text)}
.area .cities{position:absolute;left:667px;top:3986px;font-size:15px;font-weight:700;color:var(--navy)}

/* footer */
.footer{left:0;top:4220px;width:1200px;height:482px}
.footer h4{position:absolute;top:182px;font-size:16px;font-weight:700;color:var(--white);letter-spacing:.5px}
.footer .link{position:absolute;font-size:13px;color:#d8dbe4;white-space:nowrap}
.footer .fl{position:absolute;font-size:13px;color:#d8dbe4;line-height:18px;white-space:nowrap}
.footer .fl b{color:var(--white);font-weight:600}
.f-dot{position:absolute;width:26px;height:26px;border-radius:50%;background:var(--green)}
.copy{position:absolute;left:0;top:442px;width:1200px;text-align:center;font-size:12px;color:#d8dbe4}
.copy-rule{position:absolute;left:0;top:416px;width:1200px;height:1px;background:#343d5c}
</style>
</head>
<body>

<!-- top bar -->
<div class="abs topbar">
  <span class="social-dot" style="left:160px"></span>
  <span class="social-dot" style="left:188px"></span>
  <span class="social-dot" style="left:216px"></span>
  <div class="topbar-contact" style="left:624px">
    <svg width="13" height="13" viewBox="0 0 24 24" fill="#fff"><path d="M6.6 10.8a15 15 0 0 0 6.6 6.6l2.2-2.2a1 1 0 0 1 1-.25 11.4 11.4 0 0 0 3.6.6 1 1 0 0 1 1 1V20a1 1 0 0 1-1 1A17 17 0 0 1 3 4a1 1 0 0 1 1-1h3.5a1 1 0 0 1 1 1c0 1.25.2 2.45.6 3.6a1 1 0 0 1-.25 1z"/></svg><b>Phone:</b> 905-555-0147
  </div>
  <div class="topbar-contact" style="left:796px">
    <svg width="14" height="12" viewBox="0 0 24 18"><path d="M1 1h22v16H1z" fill="#fff"/><path d="M1 1l11 9 11-9" stroke="#1c2541" stroke-width="2" fill="none"/></svg><b>Email:</b> info@korvalbuilds.ca
  </div>
</div>

<!-- header -->
<div class="abs header">
  <div class="wordmark" style="left:160px;top:30px;font-size:12px;color:var(--navy)">KORVAL RENOVATIONS AND CUSTOM BUILDS</div>
  <nav class="nav">
    <a class="active" style="left:491px">HOME</a>
    <a style="left:570px">SERVICES OFFERED</a>
    <a style="left:742px">RECENT PROJECTS</a>
  </nav>
  <div class="btn" style="left:910px;top:18px;width:128px;height:37px">Contact Us</div>
</div>

<!-- hero -->
<div class="abs hero" role="img" aria-label="Photo of a bright modern kitchen with stainless appliances and bar stools">
  <h1>LET'S CONSTRUCT A<br><b>BETTER TOMORROW</b><br>FOR <b>FUTURE</b><br><b>GENERATIONS.</b></h1>
  <div class="btn" style="left:160px;top:324px;width:129px;height:37px">Contact Us</div>
</div>
<svg class="abs" style="left:0;top:560px" width="1200" height="170" viewBox="0 560 1200 170">
  <path d="M0 582 Q560 650 950 702 L1200 628 L1200 730 L0 730Z" fill="#ffffff"/>
  <path d="M460 650 Q760 690 952 702 L1200 600 L1200 616 L952 712 Q760 700 460 650Z" fill="#78b72b"/>
</svg>

<!-- who we are -->
<section class="who">
  <div class="abs who-frame"></div>
  <div class="abs who-photo" role="img" aria-label="Photo of a two-storey house with a double garage at dusk"></div>
  <svg class="abs" style="left:160px;top:1060px" width="120" height="100" viewBox="0 0 120 100"><path d="M0 0 L12 0 L12 80 Q60 88 116 88 L116 100 L0 100Z" fill="#78b72b"/></svg>
  <div class="abs badge"><div class="num">25</div><div class="lbl">YEAR OF<br>EXPERIENCE</div></div>
  <h2>WHO <span>WE ARE</span></h2>
  <div class="title-rule" style="left:672px;top:852px"></div>
  <p>A team of professionals with <b>over 25 years</b> of combined experience in all sectors of the building field with design, trades, and construction management</p>
  <div class="btn" style="left:672px;top:1088px;width:128px;height:37px">Contact Us</div>
</section>

<!-- what we do -->
<section class="what">
  <h2 class="section-title" style="top:1264px"><b>WHAT</b> WE DO</h2>
  <div class="title-rule" style="left:580px;top:1310px"></div>
  <p class="lead" style="top:1329px">We <b>DESIGN, EXECUTE,</b> And <b>MANAGE ANY CONSTRUCTION</b> Project Whether It's</p>
  <div class="sector" style="left:219px;background:linear-gradient(160deg,#4a7fc2 0%,#8fa3b8 45%,#3f4450 100%)" role="img" aria-label="Photo of a suburban family home"><span>RESIDENTIAL</span></div>
  <div class="sector" style="left:480px;background:linear-gradient(160deg,#5d9de0 0%,#1f5fa8 50%,#0d2448 100%)" role="img" aria-label="Photo of a glass office tower"><span>COMMERCIAL</span></div>
  <div class="sector" style="left:741px;background:linear-gradient(160deg,#c9b48c 0%,#8f7a5b 50%,#3a3126 100%)" role="img" aria-label="Photo of stone columns of a public building"><span>INSTITUTIONAL</span></div>
</section>

<!-- services -->
<section class="abs services">
  <h2 class="section-title" style="top:82px"><b>SERVICES</b> OFFERED</h2>
  <div class="title-rule" style="left:580px;top:128px"></div>

  <div class="card" style="left:160px;top:176px"><div class="ph" role="img" aria-label="Photo of a basement under framing" style="background:linear-gradient(180deg,#9a7b63,#5f4a3c)"></div><div class="ic"><svg width="22" height="22" viewBox="0 0 24 24" fill="none" stroke="#fff" stroke-width="2"><path d="M3 11l9-7 9 7v9H3z"/><path d="M9 20v-6h6v6"/></svg></div><div class="nm">FINISHING<br>BASEMENTS</div></div>
  <div class="card" style="left:385px;top:176px"><div class="ph" role="img" aria-label="Photo of clients shaking hands over a house model" style="background:linear-gradient(180deg,#c4c7c9,#6e6a66)"></div><div class="ic"><svg width="22" height="22" viewBox="0 0 24 24" fill="none" stroke="#fff" stroke-width="2"><path d="M3 11l9-7 9 7v9H3z"/><path d="M9 20v-6h6v6"/></svg></div><div class="nm">SECOND<br>LEGAL UNITS</div></div>
  <div class="card" style="left:610px;top:176px"><div class="ph" role="img" aria-label="Photo of a renovated empty room" style="background:linear-gradient(180deg,#b8b2aa,#5b554f)"></div><div class="ic"><svg width="22" height="22" viewBox="0 0 24 24" fill="none" stroke="#fff" stroke-width="2"><path d="M3 11l9-7 9 7v9H3z"/><path d="M9 20v-6h6v6"/></svg></div><div class="nm">COMPLETE<br>REMODELING</div></div>
  <div class="card" style="left:835px;top:176px"><div class="ph" role="img" aria-label="Photo of a brick house with an addition" style="background:linear-gradient(180deg,#5e95d6,#9a5a46 60%,#4f6b3b)"></div><div class="ic"><svg width="22" height="22" viewBox="0 0 24 24" fill="none" stroke="#fff" stroke-width="2"><path d="M3 11l9-7 9 7v9H3z"/><path d="M9 20v-6h6v6"/></svg></div><div class="nm">EXTENSIONS /<br>ADDITIONS</div></div>

  <div class="card" style="left:160px;top:444px"><div class="ph" role="img" aria-label="Photo of a dark modern kitchen" style="background:linear-gradient(180deg,#7f8287,#2d2f33)"></div><div class="ic"><svg width="22" height="22" viewBox="0 0 24 24" fill="none" stroke="#fff" stroke-width="2"><path d="M3 11l9-7 9 7v9H3z"/><path d="M9 20v-6h6v6"/></svg></div><div class="nm">KITCHEN<br>RENOVATIONS</div></div>
  <div class="card" style="left:385px;top:444px"><div class="ph" role="img" aria-label="Photo of a black marble bathroom" style="background:linear-gradient(180deg,#3a3a3c,#0e0e10)"></div><div class="ic"><svg width="22" height="22" viewBox="0 0 24 24" fill="none" stroke="#fff" stroke-width="2"><path d="M3 11l9-7 9 7v9H3z"/><path d="M9 20v-6h6v6"/></svg></div><div class="nm">BATHROOM<br>RENOVATIONS</div></div>
  <div class="card" style="left:610px;top:444px"><div class="ph" role="img" aria-label="Photo of a large custom built home" style="background:linear-gradient(180deg,#dfe3e6,#8f6a52 60%,#4e6a37)"></div><div class="ic"><svg width="22" height="22" viewBox="0 0 24 24" fill="none" stroke="#fff" stroke-width="2"><path d="M3 11l9-7 9 7v9H3z"/><path d="M9 20v-6h6v6"/></svg></div><div class="nm">CUSTOM<br>HOMES</div></div>
  <div class="card" style="left:835px;top:444px"><div class="ph" role="img" aria-label="Photo of a modern office interior" style="background:linear-gradient(180deg,#6b6e72,#c4c2bd)"></div><div class="ic"><svg width="22" height="22" viewBox="0 0 24 24" fill="none" stroke="#fff" stroke-width="2"><path d="M3 11l9-7 9 7v9H3z"/><path d="M9 20v-6h6v6"/></svg></div><div class="nm">OFFICE &amp; COMMERCIAL<br>RENOVATIONS</div></div>
</section>

<!-- team -->
<section class="team">
  <h3 style="top:2594px">OUR TEAM DOES</h3>
  <div class="task" style="left:160px;top:2640px"><svg width="14" height="14" viewBox="0 0 24 24" fill="none" stroke="#78b72b" stroke-width="3"><circle cx="12" cy="12" r="10"/><path d="M7 12l4 4 7-8"/></svg>Demolition</div>
  <div class="task" style="left:160px;top:2676px"><svg width="14" height="14" viewBox="0 0 24 24" fill="none" stroke="#78b72b" stroke-width="3"><circle cx="12" cy="12" r="10"/><path d="M7 12l4 4 7-8"/></svg>Framing</div>
  <div class="task" style="left:160px;top:2712px"><svg width="14" height="14" viewBox="0 0 24 24" fill="none" stroke="#78b72b" stroke-width="3"><circle cx="12" cy="12" r="10"/><path d="M7 12l4 4 7-8"/></svg>Fire Separation</div>
  <div class="task" style="left:160px;top:2748px"><svg width="14" height="14" viewBox="0 0 24 24" fill="none" stroke="#78b72b" stroke-width="3"><circle cx="12" cy="12" r="10"/><path d="M7 12l4 4 7-8"/></svg>Flooring</div>
  <div class="task" style="left:160px;top:2784px"><svg width="14" height="14" viewBox="0 0 24 24" fill="none" stroke="#78b72b" stroke-width="3"><circle cx="12" cy="12" r="10"/><path d="M7 12l4 4 7-8"/></svg>Trims</div>
  <div class="task" style="left:340px;top:2640px"><svg width="14" height="14" viewBox="0 0 24 24" fill="none" stroke="#78b72b" stroke-width="3"><circle cx="12" cy="12" r="10"/><path d="M7 12l4 4 7-8"/></svg>Cutting Doors / &nbsp;Windows</div>
  <div class="task" style="left:340px;top:2676px"><svg width="14" height="14" viewBox="0 0 24 24" fill="none" stroke="#78b72b" stroke-width="3"><circle cx="12" cy="12" r="10"/><path d="M7 12l4 4 7-8"/></svg>Thermal Insulation</div>
  <div class="task" style="left:340px;top:2712px"><svg width="14" height="14" viewBox="0 0 24 24" fill="none" stroke="#78b72b" stroke-width="3"><circle cx="12" cy="12" r="10"/><path d="M7 12l4 4 7-8"/></svg>Drywalling, Painting</div>
  <div class="task" style="left:340px;top:2748px"><svg width="14" height="14" viewBox="0 0 24 24" fill="none" stroke="#78b72b" stroke-width="3"><circle cx="12" cy="12" r="10"/><path d="M7 12l4 4 7-8"/></svg>Doors</div>
  <div class="task" style="left:340px;top:2784px"><svg width="14" height="14" viewBox="0 0 24 24" fill="none" stroke="#78b72b" stroke-width="3"><circle cx="12" cy="12" r="10"/><path d="M7 12l4 4 7-8"/></svg>Kitchen Cabinets</div>
  <div class="abs team-rule"></div>
  <h3 style="top:2834px">OUR SUBCONTRACTORS DO</h3>
  <div class="task" style="left:160px;top:2880px"><svg width="14" height="14" viewBox="0 0 24 24" fill="none" stroke="#78b72b" stroke-width="3"><circle cx="12" cy="12" r="10"/><path d="M7 12l4 4 7-8"/></svg>Plumbing</div>
  <div class="task" style="left:160px;top:2916px"><svg width="14" height="14" viewBox="0 0 24 24" fill="none" stroke="#78b72b" stroke-width="3"><circle cx="12" cy="12" r="10"/><path d="M7 12l4 4 7-8"/></svg>Taping</div>
  <div class="task" style="left:340px;top:2880px"><svg width="14" height="14" viewBox="0 0 24 24" fill="none" stroke="#78b72b" stroke-width="3"><circle cx="12" cy="12" r="10"/><path d="M7 12l4 4 7-8"/></svg>Electrical</div>
  <div class="task" style="left:340px;top:2916px"><svg width="14" height="14" viewBox="0 0 24 24" fill="none" stroke="#78b72b" stroke-width="3"><circle cx="12" cy="12" r="10"/><path d="M7 12l4 4 7-8"/></svg>Tilling</div>
  <div class="btn" style="left:160px;top:2970px;width:129px;height:36px">Contact Us</div>
  <div class="abs" style="left:621px;top:2590px;width:417px;height:401px;background:linear-gradient(135deg,#d9cbb4 0%,#b49a78 45%,#6f5a47 100%)" role="img" aria-label="Photo of a couple looking at a kitchen under renovation"></div>
</section>

<!-- why us -->
<section class="abs why">
  <h2 class="section-title" style="top:80px"><b>WHY</b> US</h2>
  <div class="title-rule" style="left:580px;top:126px"></div>
  <svg class="abs" style="left:410px;top:100px" width="380" height="380" viewBox="0 0 380 380"><circle cx="190" cy="192" r="178" fill="none" stroke="#c6c9d2" stroke-width="1.5" stroke-dasharray="5 5"/></svg>
  <div class="abs" style="left:481px;top:173px;width:238px;height:238px;border-radius:50%;background:linear-gradient(90deg,#6b4a35 0%,#a78b70 48%,#e6e4df 52%,#bdb7ad 100%);border:6px solid #fff" role="img" aria-label="Photo of a room half before and half after renovation"></div>
  <div class="abs" style="left:550px;top:243px;width:100px;height:100px;border-radius:50%;background:#fff;display:flex;align-items:center;justify-content:center;font-size:13px;font-weight:700;color:var(--navy)">KORVAL</div>

  <div class="why-ic" style="left:412px;top:166px"><svg width="34" height="34" viewBox="0 0 24 24" fill="none" stroke="#fff" stroke-width="1.6"><circle cx="12" cy="9" r="6"/><path d="M12 6v6M10 7.5h3a1.2 1.2 0 0 1 0 2.4h-2a1.2 1.2 0 0 0 0 2.4h3M3 20h6l4-2h6"/></svg></div>
  <div class="why-lbl" style="left:240px;top:190px;width:160px;text-align:right">Competitive Rates</div>

  <div class="why-ic" style="left:715px;top:166px"><svg width="34" height="34" viewBox="0 0 24 24" fill="none" stroke="#fff" stroke-width="1.6"><circle cx="12" cy="12" r="9"/><path d="M12 7v5l3 2"/></svg></div>
  <div class="why-lbl" style="left:799px;top:178px">Flexible Working Hours<br>(including Weekends)</div>

  <div class="why-ic" style="left:412px;top:343px"><svg width="30" height="34" viewBox="0 0 24 24" fill="none" stroke="#fff" stroke-width="1.6"><rect x="5" y="3" width="14" height="18"/><path d="M8 8h8M8 12h8M8 16h5"/></svg></div>
  <div class="why-lbl" style="left:240px;top:356px;width:160px;text-align:right">Licensed<br>Subcontractors</div>

  <div class="why-ic" style="left:715px;top:343px"><svg width="32" height="32" viewBox="0 0 24 24" fill="none" stroke="#fff" stroke-width="1.6"><rect x="4" y="3" width="14" height="18"/><path d="M7 8h8M7 12h8M7 16h4"/><circle cx="17" cy="17" r="3"/></svg></div>
  <div class="why-lbl" style="left:799px;top:356px">Suppliers List Suits<br>Every Budget</div>

  <div class="why-ic" style="left:565px;top:431px"><svg width="34" height="34" viewBox="0 0 24 24" fill="none" stroke="#fff" stroke-width="1.6"><circle cx="12" cy="6" r="2.5"/><circle cx="5" cy="9" r="2"/><circle cx="19" cy="9" r="2"/><path d="M8 20v-6a4 4 0 0 1 8 0v6M2 18v-3a3 3 0 0 1 4-2.5M22 18v-3a3 3 0 0 0-4-2.5"/></svg></div>
  <div class="why-lbl" style="left:0;top:520px;width:1200px;text-align:center">Wide Network of Consultants</div>
</section>

<!-- area we cover -->
<section class="area">
  <div class="abs" style="left:160px;top:3785px;width:452px;height:378px;background:linear-gradient(90deg,#9c9c9c 0%,#9c9c9c 52%,#78b72b 62%,#78b72b 100%);border-radius:40% 30% 45% 35%" role="img" aria-label="Map of the country with the service region highlighted and the covered towns marked"></div>
  <h2>AREA <span>WE COVER</span></h2>
  <div class="title-rule" style="left:667px;top:3910px"></div>
  <p>Lorem Ipsum is simply dummy text of the printing and typesetting industry industry's standard dummy</p>
  <div class="cities">Westbrook, Harlow Bay, Pinecrest</div>
  <div class="btn" style="left:667px;top:4040px;width:128px;height:34px">Contact Us</div>
  <div class="btn btn-navy" style="left:808px;top:4040px;width:138px;height:34px"><svg width="12" height="12" viewBox="0 0 24 24" fill="#fff" style="margin-right:5px"><path d="M6.6 10.8a15 15 0 0 0 6.6 6.6l2.2-2.2a1 1 0 0 1 1-.25 11.4 11.4 0 0 0 3.6.6 1 1 0 0 1 1 1V20a1 1 0 0 1-1 1A17 17 0 0 1 3 4a1 1 0 0 1 1-1h3.5a1 1 0 0 1 1 1c0 1.25.2 2.45.6 3.6a1 1 0 0 1-.25 1z"/></svg>905-555-0147</div>
</section>

<!-- footer -->
<footer class="abs footer">
  <svg class="abs" style="left:0;top:0" width="1200" height="482" viewBox="0 0 1200 482">
    <path d="M0 98 L260 8 L1200 60 L1200 482 L0 482Z" fill="#78b72b"/>
    <path d="M0 108 L265 20 L1200 72 L1200 482 L0 482Z" fill="#1c2541"/>
  </svg>
  <div class="copy-rule"></div>

  <h4 style="left:160px">QUICK LINKS</h4>
  <div class="link" style="left:160px;top:224px">» Home</div>
  <div class="link" style="left:160px;top:251px">» Services Offered</div>
  <div class="link" style="left:160px;top:278px">» Recent Projects</div>
  <div class="link" style="left:160px;top:305px">» Contact Us</div>

  <h4 style="left:362px">CONTACT DETAILS</h4>
  <svg class="abs" style="left:362px;top:224px" width="12" height="16" viewBox="0 0 12 16"><path d="M6 0a6 6 0 0 1 6 6c0 4-6 10-6 10S0 10 0 6a6 6 0 0 1 6-6z" fill="#fff"/><circle cx="6" cy="6" r="2" fill="#1c2541"/></svg>
  <div class="fl" style="left:384px;top:224px">Brookfield Park, ON</div>
  <svg class="abs" style="left:362px;top:266px" width="13" height="13" viewBox="0 0 24 24" fill="#fff"><path d="M6.6 10.8a15 15 0 0 0 6.6 6.6l2.2-2.2a1 1 0 0 1 1-.25 11.4 11.4 0 0 0 3.6.6 1 1 0 0 1 1 1V20a1 1 0 0 1-1 1A17 17 0 0 1 3 4a1 1 0 0 1 1-1h3.5a1 1 0 0 1 1 1c0 1.25.2 2.45.6 3.6a1 1 0 0 1-.25 1z"/></svg>
  <div class="fl" style="left:384px;top:264px"><b>Phone</b><br>905-555-0147</div>
  <svg class="abs" style="left:362px;top:312px" width="14" height="11" viewBox="0 0 24 18"><path d="M1 1h22v16H1z" fill="#fff"/><path d="M1 1l11 9 11-9" stroke="#1c2541" stroke-width="2" fill="none"/></svg>
  <div class="fl" style="left:384px;top:310px"><b>Email</b><br>info@korvalbuilds.ca</div>

  <h4 style="left:628px">FOLLOW US</h4>
  <span class="f-dot" style="left:628px;top:222px"></span><div class="link" style="left:668px;top:227px">Community</div>
  <span class="f-dot" style="left:628px;top:265px"></span><div class="link" style="left:668px;top:270px">Updates</div>
  <span class="f-dot" style="left:628px;top:308px"></span><div class="link" style="left:668px;top:313px">Videos</div>

  <div class="wordmark" style="left:816px;top:252px;font-size:12px;color:var(--white)">KORVAL RENOVATIONS AND CUSTOM BUILDS</div>

  <div class="copy">© 2022 KORVAL Renovations And Custom Builds. All Rights Reserved.</div>
</footer>

</body>
</html>
```